Cedar Ridge Clay Range wordpress theme

I want a Wordpress theme that is classy, unusual, colorful, etc. based on my attached logo files.

Font:
- Serpentine-Bold-Bold for "CEDAR RIDGE"
- BrowalliaUPC for "CLAY RANGE"

Colors (CMYK code):
- BLACK ....... 0; 0; 0; 100;
- ORANGE ... gradient from 0; 65; 97.5; 0 to 0; 39; 97.5; 0

```html
<!DOCTYPE html>
<html lang="en">
<head>
<meta charset="utf-8">
<title>Cedar Ridge Clay Range</title>
<link rel="stylesheet" href="https://fonts.googleapis.com/css2?family=Gelasio:ital,wght@0,400;0,700;1,400;1,700&display=swap">
<style>
:root{
  --black:#000;
  --page:#161616;
  --footer:#0d0d0d;
  --orange-deep:#f15a22;
  --orange:#f7941d;
  --orange-light:#f9a51b;
  --orange-text:#f7a21e;
  --white:#fff;
  --card-text:#222;
  --muted:#8d97ad;
  --news-text:#3a2a10;
  --search:#3a4150;
  --search-border:#6d7788;
  --link-current:#6f9be0;
}
*{box-sizing:border-box;margin:0;padding:0}
html,body{width:777px;height:1200px;overflow:hidden}
body{position:relative;background:var(--page);font-family:"Gelasio",Georgia,serif;color:var(--white)}
.abs{position:absolute}

.brand{left:47px;top:8px;width:113px;height:105px;display:flex;flex-direction:column;align-items:center;justify-content:center;gap:6px}
.brand-mark{width:34px;height:34px;border-radius:50%;background:var(--orange)}
.brand-name{color:var(--orange);font-weight:700;font-size:13px;line-height:1.1;text-align:center}

.search{left:537px;top:63px;width:194px;height:16px;background:var(--search);border:1px solid var(--search-border)}
.search svg{position:absolute;right:3px;top:2px}

.social{display:flex;gap:6px}
.social span{width:26px;height:26px;border-radius:50%;background:var(--orange)}
.social-top{left:618px;top:89px}

.rule{left:40px;top:124px;width:697px;height:2px;background:var(--orange-deep)}

.nav a{position:absolute;top:132px;height:23px;background:linear-gradient(var(--orange-light),var(--orange-deep));color:var(--white);font-size:9px;font-weight:700;text-decoration:none;display:flex;align-items:center;justify-content:center;letter-spacing:.3px}

.slider{left:52px;top:180px;width:667px;height:267px;background:linear-gradient(180deg,#9bb27a 0%,#6f8a4a 40%,#6b5a48 65%,#b79a74 100%)}
.slider-dots{right:4px;bottom:4px;display:flex;gap:3px}
.slider-dots i{width:7px;height:7px;border-radius:50%;background:var(--orange)}

.feature-title{top:466px;width:184px;text-align:center;color:var(--orange-text);font-weight:700;font-size:14px;line-height:17px;letter-spacing:-.2px;text-transform:uppercase;white-space:nowrap}
.card{top:503px;width:170px;height:258px;background:var(--white);padding:14px 8px 0}
.card-photo{height:99px;margin:0 2px}
.card p{margin-top:17px;font-size:9.1px;line-height:13.4px;color:var(--card-text);text-align:center}
.card .more{display:block;margin-top:9px;text-align:center;color:var(--orange-deep);font-weight:700;font-size:10px}

.col-title{top:782px;font-weight:700;font-size:13.5px;line-height:16px;text-transform:uppercase}
.col-lead{font-weight:700;font-size:10.5px;line-height:14px}
.col-body{font-size:9.6px;line-height:14px;color:var(--muted)}

.emblem{left:64px;top:862px;width:186px;height:196px;display:flex;flex-direction:column;align-items:center;justify-content:center;gap:10px}
.emblem-mark{width:70px;height:70px;border-radius:50%;background:var(--orange)}
.emblem-name{color:var(--orange);font-weight:700;font-size:24px;line-height:1.1;text-align:center}

.ticks{list-style:none}
.ticks li{position:relative;padding-left:13px;font-style:italic;font-size:9.2px;line-height:13px;color:var(--muted);margin-bottom:3px}
.ticks svg{position:absolute;left:0;top:2px}

.news{left:517px;width:205px;background:var(--orange-light);padding:7px 6px 0 26px;color:var(--news-text);font-style:italic;font-weight:700;font-size:8.6px;line-height:13px}
.news::before{content:"\201C";position:absolute;left:8px;top:0;font-size:26px;line-height:26px;color:var(--white);font-style:normal}
.news b{display:inline-block;margin-left:8px;padding:0 12px;background:var(--orange-deep);color:var(--white);font-style:normal;font-size:9.2px;line-height:13px}

.footer{left:0;top:1127px;width:777px;height:73px;background:var(--footer)}
.footer-links{left:38px;top:14px;font-size:9.5px;font-weight:700;color:var(--orange-text)}
.footer-links a{color:var(--orange-text);text-decoration:none}
.footer-links a.current{color:var(--link-current)}
.copyright{left:38px;top:28px;font-size:9px;font-weight:700}
.social-foot{left:646px;top:14px}
</style>
</head>
<body>

<header>
  <div class="abs brand"><span class="brand-mark"></span><span class="brand-name">CEDAR RIDGE<br>CLAY RANGE</span></div>
  <div class="abs search"><svg width="10" height="10" viewBox="0 0 10 10"><circle cx="4" cy="4" r="3" fill="none" stroke="#c9cfd9" stroke-width="1.3"/><path d="M6.2 6.2 9 9" stroke="#c9cfd9" stroke-width="1.4"/></svg></div>
  <div class="abs social social-top"><span></span><span></span><span></span></div>
  <div class="abs rule"></div>
  <nav class="nav">
    <a style="left:125px;width:62px">HOME</a>
    <a style="left:195px;width:78px">ABOUT US</a>
    <a style="left:281px;width:103px">OUR TEACHERS</a>
    <a style="left:392px;width:93px">OUR SERVICE</a>
    <a style="left:493px;width:90px">CONTACT US</a>
    <a style="left:593px;width:59px">BLOG</a>
  </nav>
</header>

<section class="abs slider" role="img" aria-label="Photo of a shooter aiming a scoped rifle from a bench at an outdoor range">
  <div class="abs slider-dots"><i></i><i></i><i></i></div>
</section>

<section class="features">
  <h2 class="abs feature-title" style="left:37px">Vivamus tristique<br>justo</h2>
  <h2 class="abs feature-title" style="left:210px">Aenean pulvinar<br>elit non</h2>
  <h2 class="abs feature-title" style="left:383px">Vivamus tristique<br>justo</h2>
  <h2 class="abs feature-title" style="left:557px">Aenean pulvinar<br>elit non</h2>

  <article class="abs card" style="left:44px">
    <div class="card-photo" role="img" aria-label="Photo of a shooter with ear protection aiming a shotgun" style="background:linear-gradient(135deg,#7a5a3c,#b5653a 50%,#3b2e26)"></div>
    <p>Lorem ipsum dolor sit amet, consectetur adipiscing elit. Curabitur semper tincidunt odio non vestibulum. Proin dapibus risus fermentum eros venenatis pellentesque vitae porta diam. Nunc nulla lorem, rhoncus ut egestas sed, rutrum ac nunc.</p>
    <span class="more">Read More</span>
  </article>
  <article class="abs card" style="left:217px">
    <div class="card-photo" role="img" aria-label="Photo of an instructor coaching a student with a shotgun" style="background:linear-gradient(135deg,#c9a66b,#7b6a4a 55%,#3e3324)"></div>
    <p>Lorem ipsum dolor sit amet, consectetur adipiscing elit. Curabitur semper tincidunt odio non vestibulum. Proin dapibus risus fermentum eros venenatis pellentesque vitae porta diam. Nunc nulla lorem, rhoncus ut egestas sed, rutrum ac nunc.</p>
    <span class="more">Read More</span>
  </article>
  <article class="abs card" style="left:390px">
    <div class="card-photo" role="img" aria-label="Close-up photo of brass cartridges beside a rifle action" style="background:linear-gradient(135deg,#2a2420,#5a4630 50%,#1a1614)"></div>
    <p>Lorem ipsum dolor sit amet, consectetur adipiscing elit. Curabitur semper tincidunt odio non vestibulum. Proin dapibus risus fermentum eros venenatis pellentesque vitae porta diam. Nunc nulla lorem, rhoncus ut egestas sed, rutrum ac nunc.</p>
    <span class="more">Read More</span>
  </article>
  <article class="abs card" style="left:564px">
    <div class="card-photo" role="img" aria-label="Photo of a target shooter aiming a sport rifle" style="background:linear-gradient(135deg,#d8cbb8,#8a9aa8 55%,#2f3c55)"></div>
    <p>Lorem ipsum dolor sit amet, consectetur adipiscing elit. Curabitur semper tincidunt odio non vestibulum. Proin dapibus risus fermentum eros venenatis pellentesque vitae porta diam. Nunc nulla lorem, rhoncus ut egestas sed, rutrum ac nunc.</p>
    <span class="more">Read More</span>
  </article>
</section>

<section class="about">
  <h3 class="abs col-title" style="left:56px;width:200px">Cedar Ridge Clay Range</h3>
  <p class="abs col-lead" style="left:56px;top:822px;width:200px">Lorem ipsum dolor sit amet, consec teer adipiscing. Prsent vestibulum.</p>
  <div class="abs emblem"><span class="emblem-mark"></span><span class="emblem-name">CEDAR RIDGE<br>CLAY RANGE</span></div>
</section>

<section class="support">
  <h3 class="abs col-title" style="left:283px">Care &amp; Support</h3>
  <p class="abs col-lead" style="left:283px;top:806px;width:205px">Lorem ipsum dolor sit amet, consec teer adipiscent vestibulum.</p>
  <p class="abs col-body" style="left:283px;top:842px;width:205px">Lorem ipsum dolor sit amet, conc tetur adipi scing. Praesent vestibulum molestie lacuiirhs. Aenean non ummy drerisuris. Phasellus. porta. Fusce suscipit variusium sociis totdna tibus et magis dis parturient montes, nas.</p>
  <ul class="abs ticks" style="left:287px;top:940px;width:206px">
    <li><svg width="9" height="9" viewBox="0 0 10 10"><path d="M5 0l1.5 3.3 3.5.4-2.6 2.4.7 3.5L5 7.8 1.9 9.6l.7-3.5L0 3.7l3.5-.4z" fill="#f7941d"/></svg>Lorem ipsum dolor sit amet, conc tetur adipi scing. Praesent vestibulum molestie lacuiirhs. Aenean non ummy drerisuris. Phasellus.</li>
    <li><svg width="9" height="9" viewBox="0 0 10 10"><path d="M5 0l1.5 3.3 3.5.4-2.6 2.4.7 3.5L5 7.8 1.9 9.6l.7-3.5L0 3.7l3.5-.4z" fill="#f7941d"/></svg>Lorem ipsum dolor sit amet, conc tetur adipi scing. Praesent vestibulum molestie lacuiirhs. Aenean non ummy drerisuris.</li>
    <li><svg width="9" height="9" viewBox="0 0 10 10"><path d="M5 0l1.5 3.3 3.5.4-2.6 2.4.7 3.5L5 7.8 1.9 9.6l.7-3.5L0 3.7l3.5-.4z" fill="#f7941d"/></svg>Lorem ipsum dolor sit amet, conc tetur adipi scing. Praesent vestibulum molestie lacuiirhs.</li>
    <li><svg width="9" height="9" viewBox="0 0 10 10"><path d="M5 0l1.5 3.3 3.5.4-2.6 2.4.7 3.5L5 7.8 1.9 9.6l.7-3.5L0 3.7l3.5-.4z" fill="#f7941d"/></svg>Lorem ipsum dolor sit amet, conc tetur adipi scing.</li>
  </ul>
</section>

<section class="latest">
  <h3 class="abs col-title" style="left:516px">Latest News</h3>
  <div class="abs news" style="top:813px;height:43px">Lorem ipsum dolor sit amet, conc tetur adipi scing. <b>Read More</b></div>
  <div class="abs news" style="top:872px;height:43px">Lorem ipsum dolor sit amet, conc tetur adipi scing. <b>Read More</b></div>
  <div class="abs news" style="top:929px;height:60px">Lorem ipsum dolor sit amet, conc tetur adipi scing. Praesent vestibulum molestie lacuiirhs. <b>Read More</b></div>
  <div class="abs news" style="top:1001px;height:43px">Lorem ipsum dolor sit amet, conc tetur adipi scing. <b>Read More</b></div>
  <div class="abs news" style="top:1060px;height:44px">Lorem ipsum dolor sit amet, conc tetur adipi scing. <b>Read More</b></div>
</section>

<footer class="abs footer">
  <div class="abs footer-links"><a class="current">Home</a> | <a>About Us</a> | <a>Our Teachers</a> | <a>Our Service</a> | <a>Contact Us</a> | <a>Blog</a></div>
  <div class="abs copyright">Copyright © 2014. All Rights Reserved.</div>
  <div class="abs social social-foot"><span></span><span></span><span></span></div>
</footer>

</body>
</html>
```